Flyer-Design für Ofenservice Firma
Zielgruppe
Die Firma hat als Kerngeschäft Wartung, Reinigung, Reparatur und Inbetriebnahme von Öfen und Kaminen aller Art. Der Fokus liegt dabei auf Pelletöfen. Die Firma versteht sich als zuverlässiger Dienstleister mit gutem Preisleistungsverhältnis. Zielgruppe sind hauptsächlich private Bewohner von Einfamilienhäusern in der ländlichen Gegend (Hessen)
Aufgabenstellung
Zur Bekanntmachung nach Neugründung soll ein Faltflyer gestaltet werden mit insgesamt 6 Bereichen. Die Informationen, welche auf den Flyer sollen, entnehmen Sie bitte dem Entwurf (flyer.pdf). Dieser stellt nur eine erste Idee dar und darf gerne nach Belieben verändert bzw. neu gestaltet werden. Die enthaltenen Informationen, sollten im Großen und Ganzen aber beibehalten werden. Schön wäre evtl. auch eine Hervorhebung der Preise, da wir Preisführer im Markt sind. Auch die Bilder unseres Teams sollen in den Flyer integriert sein. Auf Anfrage kann ich auch gerne weitere Kamin- und Ofenfotos zur Verfügung stellen, für welche ich die Nutzungsrechte habe. Falls Sie weitere Informationen benötigen oder Fragen haben, kommen Sie gerne auf mich zu. Die Bilder dürfen gerne etwas ausgeschnitten werden. Es geht in erster Linie darum, dass die Kunden erkennen, welche Art von Ofen sie zu Hause haben.

```html
<!DOCTYPE html>
<html lang="de">
<head>
<meta charset="utf-8">
<title>Ofenservice – Wartungsleistungen</title>
<link href="https://fonts.googleapis.com/css2?family=Open+Sans:wght@300;400;600;700&display=swap" rel="stylesheet">
<style>
  :root{
    --slate:#4b5b67;
    --slate-dark:#3a4751;
    --paper:#eff0f1;
    --paper-right:#f4f4f4;
    --ink:#3f464c;
    --head-light:#8b9397;
    --head-bold:#6b7378;
    --orange:#e1641f;
    --white:#ffffff;
  }
  *{box-sizing:border-box;margin:0;padding:0}
  html,body{width:1200px;height:860px;overflow:hidden;background:#fff}
  body{font-family:"Open Sans",Arial,sans-serif;color:var(--ink)}
  .spread{position:relative;width:1200px;height:860px;overflow:hidden}
  .panel{position:absolute;top:0;height:860px;overflow:hidden}

  /* left panel */
  .panel--pellet{left:0;width:410px;background:linear-gradient(160deg,var(--slate-dark),var(--slate) 60%);color:var(--white)}
  .panel--pellet .title{position:absolute;left:52px;top:50px;font-size:44px;line-height:46px;font-weight:300}
  .panel--pellet .title b{font-weight:700}
  .panel--pellet .intro{position:absolute;left:52px;top:157px;font-size:13px;font-weight:700}
  .panel--pellet .list{position:absolute;left:52px;top:192px;width:320px;list-style:none;font-size:13.5px;line-height:18px}
  .panel--pellet .list li{position:relative;padding-left:14px;margin-bottom:18px}
  .panel--pellet .list li::before{content:"•";position:absolute;left:0}
  .pellet-photo{position:absolute;left:0;top:0}

  /* middle panel */
  .panel--wood{left:410px;width:390px;background:var(--paper)}
  .panel--wood .title{position:absolute;left:32px;top:56px;font-size:40px;line-height:36px;color:var(--head-light);font-weight:300;letter-spacing:-.2px}
  .panel--wood .title b{color:var(--head-bold);font-weight:700;display:block}
  .panel--wood .intro{position:absolute;left:32px;top:282px;font-size:13px;font-weight:700}
  .panel--wood .list{position:absolute;left:32px;top:320px;width:325px;list-style:none;font-size:13.5px;line-height:21px}
  .panel--wood .list li{position:relative;padding-left:16px;margin-bottom:20px}
  .panel--wood .list li::before{content:"•";position:absolute;left:0;font-size:10px}
  .collage{position:absolute;left:31px;top:560px;width:329px;height:153px;display:grid;grid-template-columns:98px 124px 103px;grid-template-rows:70px 81px;gap:2px}
  .tile{display:block}
  .tile--stove{grid-row:1/3;background:linear-gradient(#2c2622,#8a5a2a 60%,#3a2e26)}
  .tile--cassette{background:linear-gradient(#6b3a26,#d2762a 55%,#2a1e18)}
  .tile--kitchen{grid-row:1/3;background:linear-gradient(#d8c98c,#b89a4a 50%,#2a2420)}
  .tile--fireplace{background:linear-gradient(#f2f0ec,#c88a3a 55%,#8a6a4a)}

  /* right panel */
  .panel--tile{left:800px;width:400px;background:var(--paper-right)}
  .tile-photo{position:absolute;left:0;top:0}
  .panel--tile .title{position:absolute;left:34px;top:303px;font-size:40px;line-height:44px;color:var(--orange);font-weight:300}
  .panel--tile .title b{font-weight:700;display:block}
  .panel--tile .list{position:absolute;left:40px;top:407px;width:310px;list-style:none;font-size:13.5px;line-height:21px;text-align:justify}
  .panel--tile .list li{position:relative;padding-left:32px;margin-bottom:20px}
  .panel--tile .list li::before{content:"";position:absolute;left:0;top:5px;width:11px;height:11px;border-radius:50%;background:var(--orange)}

  /* prices */
  .price{position:absolute;border-left:2px solid var(--orange);padding-left:16px;font-size:12px;line-height:17px;color:#222}
  .price .label{font-weight:700;font-size:12px}
  .price .deal{color:var(--orange);font-size:15px;line-height:20px}
  .price .plain small{font-size:11px}
  .price--pellet{left:52px;top:725px;width:308px;height:92px;background:rgba(255,255,255,.88);padding-top:18px}
  .price--wood{left:448px;top:735px;height:72px;padding-top:8px}
  .price--tile{left:840px;top:655px;height:150px;padding-top:8px}
  .price--tile .group + .group{margin-top:12px}
</style>
</head>
<body>
<main class="spread">

  <section class="panel panel--pellet">
    <h1 class="title">Die<br><b>Pelletöfen</b></h1>
    <p class="intro">Die Wartung beinhaltet:</p>
    <ul class="list">
      <li>Reinigung von Sichtscheibe, Brenntopf, Topfhalter, Zwischenboden, gesamter Feuerraum, sämtliche Rauchgaszüge und Aschebehälter</li>
      <li>Reinigung des Saugzuggebläses</li>
      <li>Überprüfung und Reinigung des Luftmengensensors</li>
      <li>Überprüfung der elektrischen Zündung</li>
      <li>Überprüfung der Dichtungen (Türdichtung, Türglasdichtung, Putzdeckeldichtungen)</li>
      <li>Überprüfung der Temperaturwächter</li>
      <li>Probelauf des Gerätes</li>
    </ul>
    <svg class="pellet-photo" width="410" height="860" viewBox="0 0 410 860" role="img" aria-label="Weißer Pelletofen mit brennendem Feuer vor einem Fenster mit verschneiter Berglandschaft">
      <defs>
        <linearGradient id="pelletScene" x1="0" y1="0" x2="1" y2="1">
          <stop offset="0" stop-color="#e9eef2"/>
          <stop offset=".45" stop-color="#b9a58c"/>
          <stop offset=".75" stop-color="#6d5a4a"/>
          <stop offset="1" stop-color="#3a3630"/>
        </linearGradient>
      </defs>
      <polygon points="0,530 410,625 410,860 0,860" fill="url(#pelletScene)"/>
      <line x1="0" y1="530" x2="410" y2="625" stroke="#ffffff" stroke-opacity=".7" stroke-width="2"/>
    </svg>
    <div class="price price--pellet">
      <div class="label">Preise:</div>
      <div class="deal">Mit Wartungsvertrag: 140 € inkl. MwSt</div>
      <div class="plain">Ohne Wartungsvertrag: 180 € <small>inkl. MwSt</small></div>
    </div>
  </section>

  <section class="panel panel--wood">
    <h2 class="title">Scheitholzöfen,<br>Heizkassetten,<br>Brennzellen,<b>Holz- und<br>Küchenherde</b></h2>
    <p class="intro">Die Wartung beinhaltet:</p>
    <ul class="list">
      <li>Reinigung Schamott Verkleidung, Sichtscheibe, Zwischenboden, gesamter Feuerraum, sämtliche Rauchgaszüge, Aschebehälter</li>
      <li>Reinigung der Abgasrohre (bis 2 m gestreckte Länge)</li>
      <li>Überprüfung der Dichtungen (Türdichtung, Türglas-dichtung, Putzdeckeldichtungen)</li>
      <li>Probelauf des Gerätes</li>
    </ul>
    <div class="collage">
      <span class="tile tile--stove" role="img" aria-label="Schwarzer Scheitholzofen mit Feuer"></span>
      <span class="tile tile--cassette" role="img" aria-label="Heizkassette in Backsteinwand"></span>
      <span class="tile tile--kitchen" role="img" aria-label="Holzküchenherd unter Dunstabzug"></span>
      <span class="tile tile--fireplace" role="img" aria-label="Weißer Kamin mit Brennholzstapel"></span>
    </div>
  </section>
  <div class="price price--wood">
    <div class="label">Preise:</div>
    <div class="deal">Mit Wartungsvertrag: 80 € inkl. MwSt</div>
    <div class="plain">Ohne Wartungsvertrag: 110 € <small>inkl. MwST</small></div>
  </div>

  <section class="panel panel--tile">
    <svg class="tile-photo" width="400" height="340" viewBox="0 0 400 340">
      <defs>
        <linearGradient id="tileScene" x1="0" y1="0" x2="1" y2="1">
          <stop offset="0" stop-color="#b46a22"/>
          <stop offset=".4" stop-color="#e2a35a"/>
          <stop offset=".7" stop-color="#eee8de"/>
          <stop offset="1" stop-color="#c98a4a"/>
        </linearGradient>
      </defs>
      <polygon points="0,0 400,0 400,322 0,240" fill="url(#tileScene)" role="img" aria-label="Weißer Kachelofen mit Sichtfenster in einer holzvertäfelten Stube"/>
      <polygon points="0,240 400,322 400,330 0,258" fill="var(--orange)"/>
    </svg>
    <h2 class="title">Grund-/<b>Kachelöfen</b></h2>
    <ul class="list">
      <li>Reinigung Schamott Verkleidung, Sichtscheibe, Zwischenboden, gesamter Feuerraum, sämtliche Rauchgaszüge, Aschebehälter</li>
      <li>Reinigung der Abgasrohre<br>(bis zu 2 m gestreckte Länge)</li>
      <li>Überprüfung der Dichtungen (Türdichtung, Türglasdichtung, Putzdeckeldichtungen)</li>
      <li>Probelauf des Gerätes</li>
    </ul>
  </section>
  <div class="price price--tile">
    <div class="group">
      <div class="label">Preise Kachelofen mit bis zu 4 Öffnungen</div>
      <div class="deal">Mit Wartungsvertrag: 350 € inkl. MwSt</div>
      <div class="plain">Ohne Wartungsvertrag: 390 € <small>inkl. MwSt</small></div>
    </div>
    <div class="group">
      <div class="label">Preise Kachelofen mit nachgeschalteter Heizfläche</div>
      <div class="deal">Mit Wartungsvertrag: 250 € inkl. MwSt</div>
      <div class="plain">Ohne Wartungsvertrag: 290 € <small>inkl. MwSt</small></div>
    </div>
  </div>

</main>
</body>
</html>
```